QRN Law Letterhead

Want law firm letterhead - both in terms of a pdf file that I can use electronically as letterhead by adding it as a background - and in terms of a file that I can send to a company to create actual letterhead.
Industry/Entity Type
Law Firm
Font styles to use
Sans Serif
Requirements
Must have
- Should have the following information (you can decide where to place):
- My name - Emil Vostrakian
- My email - emil@qrnlegalgroup.example
- My address - 2861 Corvella Parkway 318-742
- San Jose, California 95342
- Website - www.qrnlegalgroup.example
- Phone - 408-297-1586
- Fax - 408-853-2941
- The logo I attached
Nice to have
- I think I would prefer to have a black and white color scheme.
- I don't necessarily need a title after my name, but I have seen a few design submissions that include a generic title. The title I would use is "IP Litigator & Trademark Attorney"

```html
<!DOCTYPE html>
<html lang="en">
<head>
<meta charset="utf-8">
<title>QRN Law Letterhead</title>
<link rel="stylesheet" href="https://fonts.googleapis.com/css2?family=Lato:wght@400;700&display=swap">
<style>
  :root {
    --backdrop: #454545;
    --paper: #ffffff;
    --brand: #5d7a8c;
    --ink: #333333;
    --icon: #111111;
  }
  * { margin: 0; padding: 0; box-sizing: border-box; }
  html, body {
    width: 1200px;
    height: 1200px;
    overflow: hidden;
    background: var(--backdrop);
    font-family: "Lato", sans-serif;
  }
  .letterhead {
    position: absolute;
    left: 210px;
    top: 49px;
    width: 780px;
    height: 1102px;
    background: var(--paper);
  }
  .header-band {
    position: absolute;
    left: 0;
    top: 20px;
    width: 100%;
    height: 127px;
    background: var(--brand);
  }
  .brand-disc {
    position: absolute;
    left: 327px;
    top: 20px;
    width: 127px;
    height: 127px;
    border-radius: 50%;
    background: var(--paper);
  }
  .firm-name {
    position: absolute;
    left: 0;
    top: 150px;
    width: 100%;
    text-align: center;
    font-size: 86px;
    font-weight: 700;
    color: var(--brand);
    letter-spacing: 2px;
    line-height: 1;
  }
  .attorney-name {
    position: absolute;
    right: 65px;
    top: 274px;
    font-size: 15px;
    font-weight: 700;
    color: var(--ink);
    letter-spacing: 0.5px;
  }
  .contact-footer {
    position: absolute;
    left: 0;
    top: 1004px;
    width: 100%;
    display: flex;
    justify-content: space-between;
    padding: 0 42px;
  }
  .contact-item {
    width: 200px;
    text-align: center;
    font-size: 11px;
    line-height: 14px;
    color: var(--icon);
  }
  .contact-item svg {
    display: block;
    margin: 0 auto 14px;
    width: 36px;
    height: 34px;
  }
  .contact-item--web { font-size: 11.5px; letter-spacing: 0.3px; }
</style>
</head>
<body>
  <main class="letterhead">
    <div class="header-band"></div>
    <div class="brand-disc"></div>
    <h1 class="firm-name">QRN Law</h1>
    <p class="attorney-name">EMIL VOSTRAKIAN</p>

    <footer class="contact-footer">
      <div class="contact-item contact-item--address">
        <svg viewBox="0 0 36 34" aria-hidden="true">
          <path d="M18 2a8 8 0 0 0-8 8c0 6 8 15 8 15s8-9 8-15a8 8 0 0 0-8-8z" fill="var(--icon)"/>
          <circle cx="18" cy="10" r="3.2" fill="var(--paper)"/>
          <ellipse cx="18" cy="27" rx="14" ry="4.5" fill="none" stroke="var(--icon)" stroke-width="2"/>
        </svg>
        2861 Corvella Parkway 318-742<br>San Jose, California 95342
      </div>
      <div class="contact-item contact-item--phone">
        <svg viewBox="0 0 36 34" aria-hidden="true">
          <path d="M3 10c0-5 30-5 30 0v3h-7v-3c-4-1-12-1-16 0v3H3z" fill="var(--icon)"/>
          <path d="M9 14h18l4 14H5z" fill="var(--icon)"/>
          <g fill="var(--paper)">
            <rect x="14" y="17" width="2" height="2"/><rect x="17" y="17" width="2" height="2"/><rect x="20" y="17" width="2" height="2"/>
            <rect x="14" y="20" width="2" height="2"/><rect x="17" y="20" width="2" height="2"/><rect x="20" y="20" width="2" height="2"/>
            <rect x="14" y="23" width="2" height="2"/><rect x="17" y="23" width="2" height="2"/><rect x="20" y="23" width="2" height="2"/>
          </g>
        </svg>
        P: 408-297-1586<br>F: 408-853-2941
      </div>
      <div class="contact-item contact-item--web">
        <svg viewBox="0 0 36 34" aria-hidden="true">
          <circle cx="18" cy="15" r="13" fill="var(--icon)"/>
          <path d="M12 7c3 1 5 3 4 6s-4 2-5 5 2 5 1 7c-3-2-5-6-4-10s2-6 4-8z" fill="var(--paper)"/>
          <path d="M22 16c2 0 4 2 3 5s-3 3-4 1 0-6 1-6z" fill="var(--paper)"/>
        </svg>
        emil@qrnlegalgroup.example<br>www.qrnlegalgroup.example
      </div>
    </footer>
  </main>
</body>
</html>
```